Bulk Food Container sticker

Our company sells bulk snacks to office locations. We re-package all sorts of foods into re-usable "Stowvessa" type containers for consistency. We need to create a designed sticker which has room to laser-print the name of the food. The "blank" sticker needs to be designed with our logo, etc... I have attached 2 files. The first is an example from another company doing a similar work, and the second is the template from the company that will be printing the stickers for me. See our website for examples of our current corporate identity. www.brightmoorbeans.com
Target Market(s)
Offices, tech companies
Industry/Entity Type
Printing
Look and feel
Each slider illustrates characteristics of the customer's brand and the style your logo design should communicate.

```html
<!DOCTYPE html>
<html lang="en">
<head>
<meta charset="utf-8">
<title>Brightmoor Beans – Bulk Container Sticker Sheet</title>
<link rel="stylesheet" href="https://fonts.googleapis.com/css2?family=Arimo:wght@400;700&display=swap">
<style>
  :root {
    --page: #ffffff;
    --page-edge: #5a1a1a;
    --orange: #e85400;
    --band: #b94600;
    --brown: #943c00;
    --ink: #6e2a00;
    --tagline: #e07a2a;
    --label-edge: #3a1a0a;
    --write-area: #ffffff;
    --small-edge: #5a2a2a;
  }
  * { box-sizing: border-box; margin: 0; padding: 0; }
  html, body { width: 929px; height: 1200px; overflow: hidden; background: var(--page); }
  .sheet {
    position: relative;
    width: 929px;
    height: 1200px;
    border: 1.5px solid var(--page-edge);
    background: var(--page);
    font-family: "Arimo", Arial, sans-serif;
  }
  .label-grid {
    position: absolute;
    left: 15px;
    top: 54px;
    display: grid;
    grid-template-columns: repeat(3, 297px);
    grid-template-rows: repeat(3, 298px);
    column-gap: 0;
    row-gap: 29px;
  }
  .container-label {
    position: relative;
    width: 297px;
    height: 298px;
    border: 1.5px solid var(--label-edge);
    border-radius: 8px;
    background: var(--brown);
    overflow: hidden;
  }
  .brand-band {
    height: 75px;
    background: var(--orange);
    display: flex;
    align-items: flex-end;
    padding: 0 0 8px 16px;
  }
  .brand-name {
    font-weight: 700;
    font-size: 32px;
    letter-spacing: -0.5px;
    color: var(--ink);
    line-height: 1;
    white-space: nowrap;
  }
  .tagline-band {
    height: 32px;
    background: var(--band);
    text-align: right;
    padding: 5px 10px 0 0;
  }
  .tagline {
    font-size: 11px;
    letter-spacing: 3px;
    color: var(--tagline);
  }
  .write-area {
    position: absolute;
    left: 18px;
    right: 12px;
    top: 141px;
    height: 143px;
    background: var(--write-area);
    border-radius: 10px;
    box-shadow: 0 0 0 2px rgba(255,255,255,0.35);
  }
  .tag-grid {
    position: absolute;
    left: 15px;
    top: 1023px;
    display: grid;
    grid-template-columns: repeat(6, 148px);
    grid-template-rows: repeat(2, 55px);
    row-gap: 11px;
  }
  .small-tag {
    border: 1.5px solid var(--small-edge);
    border-radius: 8px;
    background: var(--page);
  }
</style>
</head>
<body>
<main class="sheet">
  <section class="label-grid">
    <article class="container-label"><header class="brand-band"><span class="brand-name">Brightmoor Beans</span></header><div class="tagline-band"><span class="tagline">COFFEE SERVICE</span></div><div class="write-area"></div></article>
    <article class="container-label"><header class="brand-band"><span class="brand-name">Brightmoor Beans</span></header><div class="tagline-band"><span class="tagline">COFFEE SERVICE</span></div><div class="write-area"></div></article>
    <article class="container-label"><header class="brand-band"><span class="brand-name">Brightmoor Beans</span></header><div class="tagline-band"><span class="tagline">COFFEE SERVICE</span></div><div class="write-area"></div></article>
    <article class="container-label"><header class="brand-band"><span class="brand-name">Brightmoor Beans</span></header><div class="tagline-band"><span class="tagline">COFFEE SERVICE</span></div><div class="write-area"></div></article>
    <article class="container-label"><header class="brand-band"><span class="brand-name">Brightmoor Beans</span></header><div class="tagline-band"><span class="tagline">COFFEE SERVICE</span></div><div class="write-area"></div></article>
    <article class="container-label"><header class="brand-band"><span class="brand-name">Brightmoor Beans</span></header><div class="tagline-band"><span class="tagline">COFFEE SERVICE</span></div><div class="write-area"></div></article>
    <article class="container-label"><header class="brand-band"><span class="brand-name">Brightmoor Beans</span></header><div class="tagline-band"><span class="tagline">COFFEE SERVICE</span></div><div class="write-area"></div></article>
    <article class="container-label"><header class="brand-band"><span class="brand-name">Brightmoor Beans</span></header><div class="tagline-band"><span class="tagline">COFFEE SERVICE</span></div><div class="write-area"></div></article>
    <article class="container-label"><header class="brand-band"><span class="brand-name">Brightmoor Beans</span></header><div class="tagline-band"><span class="tagline">COFFEE SERVICE</span></div><div class="write-area"></div></article>
  </section>
  <section class="tag-grid">
    <div class="small-tag"></div><div class="small-tag"></div><div class="small-tag"></div>
    <div class="small-tag"></div><div class="small-tag"></div><div class="small-tag"></div>
    <div class="small-tag"></div><div class="small-tag"></div><div class="small-tag"></div>
    <div class="small-tag"></div><div class="small-tag"></div><div class="small-tag"></div>
  </section>
</main>
</body>
</html>
```